bramblegate crest roofing flyer*

I need an a5 size flyer designing to go in our local advertising magazine.We are based in the north west of England Id like key features from the website including on the flyer, possibly even reviews, what we do ect.I don't however want it too busy, simple pictures and description of service.company colours and logo. I require simple one sided business cards toonumber, web address and logowinner will receive a request to design around 5 different double sided a5 flyers too, each with all our services on one side and the other primarily for one service we have provided locally with a spacve to put the house number down.REPAIRSROOFLINEFLAT ROOFS PITCHED ROOFSSYNTHETIC ROOFSUP TO 50 YEARS WARRANTY AVAILABLERANKED THE #1 FLAT ROOFER IN THE UK OUT OF 787 REGISTERED FLAT ROOFING COMPANIESRANKED THE #10 ROOFING COMPANY IN THE UK OUT OF 1976 REGISTERED SPECIALIST ROOFING COMPANIESBOTH FOR COST, CUSTOMER SERVICE AND QUALITY WITH 5 STAR REVIEWSGUARANTEED TO FIND AND FIX A LEAKAPPROVED INSTALLERSAWARD WINNINGTIME SERVED FIXED PRICES

Target Market(s)

homeowners

Colors

Designer to choose only greyscale colors for use in the design.

Requirements
Must have
• contact details
• pictures of my work
• clear and simple

```html
<!DOCTYPE html>
<html lang="en">
<head>
<meta charset="utf-8">
<title>Bramblegate Crest Roofing – Business Card</title>
<link rel="stylesheet" href="https://fonts.googleapis.com/css2?family=Montserrat:wght@500;600;700;800&display=swap">
<style>
  :root {
    --green: #3f9b45;
    --yellow: #f5c116;
    --dark: #262626;
    --dark-soft: #2f2f2f;
    --white: #ffffff;
    --paper: #ececec;
    --light-grey: #e4e4e4;
    --ink: #1e1e1e;
  }
  * { box-sizing: border-box; margin: 0; padding: 0; }
  html, body {
    width: 1173px; height: 1200px; overflow: hidden;
    background: var(--paper);
    font-family: "Montserrat", sans-serif;
  }
  .card {
    position: absolute; left: 136px;
    width: 900px; height: 540px; overflow: hidden;
    box-shadow: 0 4px 14px rgba(0,0,0,.18);
  }
  .card--front { top: 40px; background: var(--white); }
  .card--back { top: 620px; background: var(--dark); }

  /* front */
  .front-art { position: absolute; inset: 0; }
  .brand-name {
    position: absolute; color: var(--green);
    font-weight: 800; text-transform: uppercase; line-height: 1.02;
  }
  .card--front .brand-name { left: 50px; top: 82px; font-size: 44px; letter-spacing: .5px; }
  .warranty-copy { position: absolute; left: 47px; top: 300px; }
  .warranty-copy__headline {
    color: var(--yellow); font-weight: 700; font-size: 37px; line-height: 1.1;
  }
  .warranty-copy__sub {
    margin-top: 10px; color: var(--white); font-weight: 700; font-size: 25px; line-height: 1.4;
  }

  /* back */
  .back-art { position: absolute; inset: 0; }
  .tagline {
    position: absolute; top: 56px; left: 0; right: 0;
    display: flex; align-items: center; gap: 14px;
    color: var(--white); font-weight: 600; font-size: 25px;
  }
  .tagline::before, .tagline::after {
    content: ""; height: 2px; background: var(--yellow); flex: 1;
  }
  .tagline::before { flex: 0 0 302px; }
  .phone-badge {
    position: absolute; left: 106px; top: 203px;
    width: 102px; height: 102px; border-radius: 50%;
    background: var(--yellow); display: flex; align-items: center; justify-content: center;
  }
  .cta { position: absolute; left: 224px; top: 186px; }
  .cta__label { color: var(--green); font-weight: 700; font-size: 49px; line-height: 1; }
  .cta__number { color: var(--white); font-weight: 700; font-size: 70px; line-height: 1.05; letter-spacing: -1px; }
  .card--back .brand-name { left: 70px; top: 395px; font-size: 30px; }
  .web-band {
    position: absolute; left: 414px; top: 409px;
    width: 486px; height: 72px;
  }
  .web-band svg { position: absolute; inset: 0; }
  .web-band__text { position: absolute; left: 64px; top: 12px; line-height: 1.2; }
  .web-band__label { color: var(--green); font-weight: 700; font-size: 19px; }
  .web-band__url { color: var(--ink); font-weight: 700; font-size: 19px; }
</style>
</head>
<body>

<section class="card card--front">
  <svg class="front-art" viewBox="0 0 900 540" width="900" height="540">
    <defs>
      <linearGradient id="brickGrad" x1="0" y1="0" x2="1" y2="1">
        <stop offset="0" stop-color="#b9c9d9"/><stop offset=".5" stop-color="#a8573a"/><stop offset="1" stop-color="#6e3a28"/>
      </linearGradient>
      <linearGradient id="ridgeGrad" x1="0" y1="0" x2="1" y2="1">
        <stop offset="0" stop-color="#5d6262"/><stop offset=".55" stop-color="#8e9292"/><stop offset="1" stop-color="#b3b5b3"/>
      </linearGradient>
      <linearGradient id="houseGrad" x1="0" y1="0" x2="0" y2="1">
        <stop offset="0" stop-color="#9a8f95"/><stop offset=".5" stop-color="#8a7f87"/><stop offset="1" stop-color="#8f7558"/>
      </linearGradient>
    </defs>
    <polygon points="760,0 900,0 900,130" fill="var(--light-grey)"/>
    <rect x="0" y="488" width="900" height="52" fill="var(--yellow)"/>
    <polygon points="0,273 611,273 676,378 611,482 0,482" fill="var(--green)"/>
    <g role="img" aria-label="Photo of a red brick house with a new roof">
      <rect x="537" y="37" width="170" height="170" rx="26" transform="rotate(45 622 122)" fill="url(#brickGrad)"/>
    </g>
    <g role="img" aria-label="Photo of a grey tiled roof ridge">
      <rect x="634" y="156" width="260" height="260" rx="30" transform="rotate(45 764 286)" fill="url(#ridgeGrad)"/>
    </g>
    <g role="img" aria-label="Photo of a terraced house with a slate roof">
      <rect x="597" y="354" width="170" height="170" rx="26" transform="rotate(45 682 439)" fill="url(#houseGrad)"/>
    </g>
  </svg>
  <div class="brand-name">Bramblegate<br>Crest Roofing</div>
  <div class="warranty-copy">
    <p class="warranty-copy__headline">UP TO 50 YEARS<br>WARRANTY AVAILABLE</p>
    <p class="warranty-copy__sub">GUARANTEED TO FIND AND<br>FIX A LEAK</p>
  </div>
</section>

<section class="card card--back">
  <svg class="back-art" viewBox="0 0 900 540" width="900" height="540" role="img" aria-label="Faint photo of a house roof behind the card content">
    <defs>
      <linearGradient id="shadeGrad" x1="0" y1="0" x2="1" y2="1">
        <stop offset="0" stop-color="var(--dark-soft)"/><stop offset="1" stop-color="var(--dark)"/>
      </linearGradient>
    </defs>
    <rect width="900" height="540" fill="url(#shadeGrad)"/>
  </svg>
  <p class="tagline">Approved Installers</p>
  <div class="phone-badge">
    <svg width="48" height="48" viewBox="0 0 24 24" aria-hidden="true">
      <path fill="var(--ink)" d="M6.6 10.8a15.1 15.1 0 0 0 6.6 6.6l2.2-2.2c.3-.3.7-.4 1-.2 1.1.4 2.3.6 3.6.6.6 0 1 .4 1 1V20c0 .6-.4 1-1 1A17 17 0 0 1 3 4c0-.6.4-1 1-1h3.5c.6 0 1 .4 1 1 0 1.3.2 2.5.6 3.6.1.3 0 .7-.2 1l-2.3 2.2z"/>
    </svg>
  </div>
  <div class="cta">
    <p class="cta__label">BOOK AN INSPECTION</p>
    <p class="cta__number">07700 900 418</p>
  </div>
  <div class="brand-name">Bramblegate<br>Crest Roofing</div>
  <div class="web-band">
    <svg viewBox="0 0 486 72" width="486" height="72" aria-hidden="true">
      <polygon points="14,0 486,0 486,72 14,72 0,36" fill="var(--yellow)"/>
      <g fill="none" stroke="var(--ink)" stroke-width="2">
        <circle cx="36" cy="37" r="14"/>
        <ellipse cx="36" cy="37" rx="6" ry="14"/>
        <line x1="22" y1="37" x2="50" y2="37"/>
        <line x1="25" y1="29" x2="47" y2="29"/>
        <line x1="25" y1="45" x2="47" y2="45"/>
      </g>
    </svg>
    <div class="web-band__text">
      <p class="web-band__label">Visit Our Website</p>
      <p class="web-band__url">www.bramblegatecrestroofing.com</p>
    </div>
  </div>
</section>

</body>
</html>
```